R. T. HOLLOWAY, INC. is a US based Investment firm looking for a five-page website design.

Currently, their temporary site is located at: rtholloway.example and they would like to maintain the site design as much as possible.

R. T. HOLLOWAY, INC. sister companies are: Crestway Lodge Investments (c-lodge.example) Benwick Petroleum (benwick-petroleum.example) and RTHF (rth-foundation.example/en)

Attached is a .ZIP file with designs and assets we think will be useful for your proposal… Content for the site is attached on: rtholloway website content.docx Current temp website design is attached as: Coming Soon Website.zip .EPS Logo files attached as: rtholloway logos.zip Sample business card attached as: R T Holloway Business cards.eps Other assets, such as Fonts and background images attached as: Assets.zip

Target Market(s)

Investors

Industry/Entity Type

Investments

Number of Pages Required

5+ page

Requirements
Must have
• Contact Page with a form.

```html
<!DOCTYPE html>
<html lang="en">
<head>
<meta charset="utf-8">
<title>R. T. Holloway, Inc.</title>
<link rel="stylesheet" href="https://fonts.googleapis.com/css2?family=Cinzel:wght@400;600&family=Montserrat:wght@400;500;600;700&display=swap">
<style>
:root{
  --navy:#1c2436;
  --navy-deep:#141a29;
  --gold:#b3975a;
  --gold-light:#c9b27c;
  --cream:#f3f0e8;
  --ink:#2a2a2a;
  --muted:#6b6b6b;
  --footer:#141414;
  --white:#ffffff;
}
*{margin:0;padding:0;box-sizing:border-box}
html,body{width:1200px;height:4784px;overflow:hidden}
body{font-family:"Montserrat",sans-serif;color:var(--ink);background:var(--white);position:relative}
.section{position:absolute;left:0;width:1200px;overflow:hidden}
.heading{font-family:"Cinzel",serif;font-weight:400;letter-spacing:3px}
.accent{color:var(--gold)}
.btn{display:inline-block;background:var(--navy);color:var(--white);font-size:11px;font-weight:700;letter-spacing:2px;text-transform:uppercase;padding:14px 30px;border-radius:30px}
.body-text{font-size:13px;line-height:1.75;color:var(--muted)}

/* hero */
.hero{top:0;height:880px}
.hero-photo{position:absolute;inset:0;background:linear-gradient(180deg,#2a3247 0%,#3b3f4c 40%,#8a6a3e 70%,#2a2c36 100%)}
.hero-shade{position:absolute;inset:0;background:rgba(18,22,34,.45)}
.nav{position:absolute;top:26px;left:0;width:1200px;height:56px}
.nav-mark{position:absolute;left:120px;top:8px;width:40px;height:40px;border:2px solid var(--white);border-radius:50%}
.nav-links{position:absolute;left:270px;top:22px;display:flex;gap:0;width:740px;justify-content:space-between}
.nav-links a{color:var(--white);font-size:10px;font-weight:600;letter-spacing:2px;text-transform:uppercase;text-decoration:none}
.nav-cta{position:absolute;right:46px;top:10px;background:var(--white);color:var(--navy);font-size:10px;font-weight:700;letter-spacing:2px;padding:12px 24px;border-radius:24px}
.hero-brand{position:absolute;top:250px;width:1200px;text-align:center}
.hero-circle{width:74px;height:74px;border:3px solid var(--gold);border-radius:50%;margin:0 auto 36px}
.hero-name{font-family:"Cinzel",serif;font-size:58px;color:var(--white);letter-spacing:6px;font-weight:400}
.hero-inc{font-family:"Cinzel",serif;font-size:36px;color:var(--gold);letter-spacing:3px;margin-top:-2px}
.hero-tag{font-size:14px;color:var(--white);line-height:1.6;margin-top:26px}
.hero-curve{position:absolute;left:0;bottom:0}

/* about */
.about{top:880px;height:680px}
.about-title{position:absolute;left:125px;top:90px;font-size:56px;color:var(--navy)}
.about-text{position:absolute;left:125px;top:200px;width:420px;font-size:11.5px}
.about-text p+p{margin-top:18px}
.about .btn{position:absolute;left:125px;top:470px}
.about-photo{position:absolute;left:680px;top:60px;width:400px;height:290px;background:linear-gradient(135deg,#dfe6ee,#a9b8c8 55%,#4d5d72)}
.about-photo-small{position:absolute;left:590px;top:330px;width:160px;height:150px;background:linear-gradient(160deg,#3c4c66,#c99a4b 60%,#1f2940);border:6px solid var(--white)}
.divider-dot{position:absolute;left:596px;width:8px;height:8px;border-radius:50%;background:var(--gold)}

/* values */
.values{top:1560px;height:840px;background:var(--navy)}
.values-title{position:absolute;right:150px;top:95px;font-size:56px;color:var(--white)}
.values-text{position:absolute;left:220px;top:200px;width:860px;text-align:center;font-size:12px;line-height:1.8;color:#c9ccd4}
.values-band{position:absolute;left:600px;top:335px;width:600px;height:250px;background:var(--gold)}
.values-grid{position:absolute;left:660px;top:365px;display:grid;grid-template-columns:260px 220px;row-gap:34px}
.value{display:flex;align-items:center;gap:18px;color:var(--white);font-size:11px;font-weight:600;letter-spacing:1px}
.value .ico{width:40px;height:40px;border-radius:50%;background:var(--white);display:flex;align-items:center;justify-content:center}

/* areas */
.areas{top:2400px;height:1180px;background:var(--cream)}
.areas-title{position:absolute;width:1200px;top:70px;text-align:center;font-size:56px;color:var(--navy)}
.areas-text{position:absolute;left:230px;top:165px;width:740px;text-align:center;font-size:12px;line-height:1.75}
.area{position:absolute;width:290px;text-align:center}
.area-photo{width:290px;height:290px;border-radius:50%}
.area-badge{position:absolute;left:0;top:210px;width:66px;height:66px;border-radius:50%;background:var(--gold);border:4px solid var(--cream)}
.area-name{font-family:"Cinzel",serif;font-size:22px;letter-spacing:3px;color:var(--navy);margin-top:18px}
.areas .btn{position:absolute;left:493px;top:1068px}

/* social */
.social{top:3580px;height:640px;background:linear-gradient(90deg,#b09356,#c5ab74 60%,#b89c61)}
.social-title{position:absolute;left:125px;top:120px;font-size:56px;line-height:1.05;color:var(--white)}
.social-text{position:absolute;left:125px;top:310px;width:400px;font-size:11.5px;line-height:1.75;color:#f6efe0}
.social .btn{position:absolute;left:125px;top:470px}

/* footer */
.footer{top:4220px;height:564px;background:var(--footer);color:#d6d6d6}
.foot-col-title{font-family:"Cinzel",serif;font-size:20px;letter-spacing:2px;color:var(--white)}
.quick{position:absolute;left:150px;top:170px;width:160px;text-align:right}
.quick ul{list-style:none;margin-top:26px}
.quick li{font-size:11px;margin-bottom:18px;color:#bdbdbd}
.foot-brand{position:absolute;left:0;top:80px;width:1200px;text-align:center}
.foot-circle{width:60px;height:60px;border:2px solid var(--gold);border-radius:50%;margin:0 auto 18px}
.foot-name{font-family:"Cinzel",serif;font-size:40px;letter-spacing:4px;color:var(--white)}
.foot-inc{font-family:"Cinzel",serif;font-size:26px;color:var(--gold)}
.newsletter{position:absolute;left:410px;top:290px;width:380px;height:44px;background:var(--white);border-radius:24px;font-size:11px;color:#999;padding:15px 24px}
.newsletter svg{position:absolute;right:18px;top:13px}
.socials{position:absolute;left:543px;top:370px;display:flex;gap:14px}
.socials span{width:30px;height:30px;border-radius:50%;background:var(--gold)}
.contact{position:absolute;left:890px;top:170px;width:220px}
.contact dl{margin-top:26px;font-size:11px;line-height:1.6}
.contact dt{color:var(--white);font-weight:700}
.contact dd{color:#bdbdbd;margin-bottom:12px}
.copyright{position:absolute;left:0;top:500px;width:1200px;text-align:center;font-size:10px;color:#9a9a9a;border-top:1px solid #2b2b2b;padding-top:24px}
.to-top{position:absolute;right:60px;top:510px;width:40px;height:40px;border-radius:50%;background:var(--gold);display:flex;align-items:center;justify-content:center}
</style>
</head>
<body>

<header class="section hero">
  <div class="hero-photo" role="img" aria-label="City skyline of glass towers at sunset"></div>
  <div class="hero-shade"></div>
  <nav class="nav">
    <div class="nav-mark"></div>
    <div class="nav-links">
      <a href="#about">About Us</a>
      <a href="#areas">Investment Areas</a>
      <a href="#social">Social Responsibility</a>
      <a href="#contact">Contact Us</a>
    </div>
    <span class="nav-cta">GET A QUOTE</span>
  </nav>
  <div class="hero-brand">
    <div class="hero-circle"></div>
    <h1 class="hero-name">R. T. HOLLOWAY</h1>
    <div class="hero-inc">Inc.</div>
    <p class="hero-tag">R. T. Holloway, Inc. helps develop into a great nation and, with<br>experience, plans its footprint worldwide.</p>
  </div>
  <svg class="hero-curve" width="1200" height="170" viewBox="0 0 1200 170">
    <path d="M0 60 C 300 180, 700 150, 1200 40 L1200 170 L0 170 Z" fill="#ffffff"/>
    <path d="M0 60 C 300 180, 700 150, 1200 40" fill="none" stroke="#b3975a" stroke-width="2"/>
  </svg>
</header>

<section class="section about" id="about">
  <h2 class="heading about-title">About <span class="accent">Us</span></h2>
  <div class="body-text about-text">
    <p>Based in Houston, Texas, R. T. Holloway, Inc. is an investment company founded in 2019, with the purpose to foster profitable, reliable development, and create platforms for increasing the potential of wealth resources designed to meet the demands of the emerging markets. R. T. Holloway, Inc. functions as a vehicle that enables investments, with the goal of developing the multiple opportunities available.</p>
    <p>R. T. Holloway, Inc. holds interests in areas of investment that are vital to the international economy: Sectors of Energy, Mining, Industry, Finance and Real Estate.</p>
  </div>
  <span class="btn">Get a quote</span>
  <div class="about-photo" role="img" aria-label="Two colleagues reviewing work on a laptop"></div>
  <div class="about-photo-small" role="img" aria-label="Glass office building seen from below"></div>
</section>

<section class="section values">
  <h2 class="heading values-title">Our Values</h2>
  <p class="values-text">Lorem Ipsum is simply dummy text of the printing and typesetting industry. Lorem Ipsum has been the industry's standard dummy text ever since the 1500s, when an unknown printer took a galley of type and scrambled it to make a type specimen book. It has survived not only five centuries, but also the leap into electronic typesetting, remaining essentially unchanged.</p>
  <div class="values-band"></div>
  <div class="values-grid">
    <div class="value"><span class="ico"><svg width="16" height="16"><path d="M3 13 L11 5 M9 3 L13 7" stroke="#b3975a" stroke-width="2"/></svg></span>Innovation</div>
    <div class="value"><span class="ico"><svg width="16" height="16"><path d="M3 8 L7 12 L13 4" stroke="#b3975a" stroke-width="2" fill="none"/></svg></span>Integrity</div>
    <div class="value"><span class="ico"><svg width="16" height="16"><path d="M8 2 L14 14 L2 14 Z" stroke="#b3975a" stroke-width="2" fill="none"/></svg></span>Organization</div>
    <div class="value"><span class="ico"><svg width="16" height="16"><path d="M8 1 L10 6 L15 6 L11 9 L12.5 14 L8 11 L3.5 14 L5 9 L1 6 L6 6 Z" fill="#b3975a"/></svg></span>Excellence</div>
    <div class="value"><span class="ico"><svg width="16" height="16"><circle cx="7" cy="7" r="4.5" stroke="#b3975a" stroke-width="2" fill="none"/><path d="M10 10 L14 14" stroke="#b3975a" stroke-width="2"/></svg></span>Transparency</div>
    <div class="value"><span class="ico"><svg width="16" height="16"><circle cx="8" cy="5" r="3" fill="#b3975a"/><path d="M2 15 C2 9,14 9,14 15 Z" fill="#b3975a"/></svg></span>Responsibility</div>
  </div>
</section>

<section class="section areas" id="areas">
  <h2 class="heading areas-title">Investment <span class="accent">Areas</span></h2>
  <p class="body-text areas-text">Lorem Ipsum is simply dummy text of the printing and typesetting industry. Lorem Ipsum has been the industry's standard dummy text ever since the 1500s, when an unknown printer took a galley of type and scrambled it to make a type specimen book. It has survived not only five centuries, but also the leap into electronic typesetting, remaining essentially unchanged.</p>
  <div class="area" style="left:143px;top:265px"><div class="area-photo" role="img" aria-label="Wind turbines on a hill at sunset" style="background:linear-gradient(180deg,#7aa3c9,#d9a66b 70%,#5a6b3a)"></div><span class="area-badge"></span><div class="area-name">Energy</div></div>
  <div class="area" style="left:455px;top:265px"><div class="area-photo" role="img" aria-label="Large mining dump truck on a dirt road" style="background:linear-gradient(180deg,#c9b89c,#c78a2c 55%,#6e5a44)"></div><span class="area-badge"></span><div class="area-name">Mining</div></div>
  <div class="area" style="left:767px;top:265px"><div class="area-photo" role="img" aria-label="Industrial plant lit at dusk" style="background:linear-gradient(180deg,#3a4f7a,#e0965a 60%,#2b2f3c)"></div><span class="area-badge"></span><div class="area-name">Industry</div></div>
  <div class="area" style="left:143px;top:665px"><div class="area-photo" role="img" aria-label="Hands holding a red heart" style="background:radial-gradient(circle at 50% 50%,#c8332f 0 22%,#cfe0ee 45%,#8fb4d6)"></div><span class="area-badge"></span><div class="area-name">Healthcare</div></div>
  <div class="area" style="left:455px;top:665px"><div class="area-photo" role="img" aria-label="Stacks of coins" style="background:linear-gradient(180deg,#2b3345,#9a8a6a 55%,#3b3426)"></div><span class="area-badge"></span><div class="area-name">Finance</div></div>
  <div class="area" style="left:767px;top:665px"><div class="area-photo" role="img" aria-label="Modern glass skyscrapers against blue sky" style="background:linear-gradient(180deg,#dfe9f4,#7f9bbd 55%,#35475f)"></div><span class="area-badge"></span><div class="area-name">Real Estate</div></div>
  <span class="btn">View all areas</span>
</section>

<section class="section social" id="social">
  <div role="img" aria-label="Faded photo of people working together" style="position:absolute;inset:0;background:linear-gradient(90deg,rgba(255,255,255,0),rgba(255,255,255,.12) 60%,rgba(0,0,0,.05))"></div>
  <h2 class="heading social-title">Social<br>Responsibility</h2>
  <p class="social-text">Since the commencement of our activity, R. T. Holloway, Inc. contributes to improve the quality of life of citizens and women across the world, through projects that support the already deprived and keep resettlement, which are beyond to do the right of basic human needs.</p>
  <span class="btn">Read more</span>
</section>

<footer class="section footer" id="contact">
  <div class="quick">
    <h3 class="foot-col-title">Quick Link</h3>
    <ul><li>Home</li><li>About Us</li><li>Investment Areas</li><li>Social Responsibility</li><li>Contact Us</li></ul>
  </div>
  <div class="foot-brand">
    <div class="foot-circle"></div>
    <div class="foot-name">R. T. HOLLOWAY</div>
    <div class="foot-inc">Inc.</div>
  </div>
  <div class="newsletter">Email address
    <svg width="18" height="18" viewBox="0 0 18 18"><path d="M1 8 L17 1 L11 17 L8 10 Z" fill="#b3975a"/></svg>
  </div>
  <div class="socials"><span></span><span></span><span></span></div>
  <div class="contact">
    <h3 class="foot-col-title">Contact</h3>
    <dl>
      <dt>Location</dt><dd>1200 Harbor Point Ave, Suite 300,<br>Houston, TX 77000, United States</dd>
      <dt>Call Us</dt><dd>+1 (000) 555-0100</dd>
      <dt>Email</dt><dd>info@rtholloway.example</dd>
    </dl>
  </div>
  <p class="copyright">Copyright © 2020. All Rights Reserved</p>
  <span class="to-top"><svg width="14" height="14"><path d="M2 10 L7 4 L12 10" stroke="#fff" stroke-width="2" fill="none"/></svg></span>
</footer>

</body>
</html>
```